Team Member Spotlight 'Stats Card' Design for ProLinkr

We are creating a 'Stats Card'-style team member spotlight post for our company's ProLinkr page. The design should be professional yet fun, reflecting our company's approachable and innovative brand. Here’s what we need:

Header featuring:
Name: Cole Banner
Role: Area Sales Manager - Austin, TX
Photo: Will provide
Quick stats section with bold, modern fonts:
Years in Pain Management: 8 years
Time at ORLO SPAN KT: 1 year (by February)
Favorite Quote: “Nothing in the world can take the place of persistence.” – Harold Pemberton
Hobby/Passion: Making music (on Tunevo as Cole Banner!)
Football Team: Ridgeford State (Hawklets)

Use vibrant, approachable company branding colors.
Incorporate small themed icons (e.g., music notes, football elements).
Clean, modern layout with clear sections and engaging visuals.
Subtle background details that hint at music and Texas without overpowering the content.

Optimized for ProLinkr dimensions (square or portrait format).
Delivered in editable file formats (Plyra) for future use.

Professional but approachable.
Engaging design that will catch attention while staying on-brand.
We will provide the company branding guide, Cole’s photo, and detailed stats. The design should feel cohesive with our brand and stand out on ProLinkr.

Industry/Entity Type

Medical Device / Physicians

Colors

Designer to choose colors to be used in the design.

Requirements
Must have
• Include ORLO SPAN KT logo & Company Colors: #a9218f & #011842

```html
<!DOCTYPE html>
<html lang="en">
<head>
<meta charset="utf-8">
<title>Team Spotlight – Cole Banner</title>
<link rel="stylesheet" href="https://fonts.googleapis.com/css2?family=Oswald:wght@300;400;500;600;700&display=swap">
<style>
  :root {
    --magenta: #a9218f;
    --navy: #011842;
    --white: #ffffff;
    --ink: #0a0a0a;
  }
  * { margin: 0; padding: 0; box-sizing: border-box; }
  html, body { width: 971px; height: 1200px; overflow: hidden; background: var(--white); }
  .spotlight-card {
    position: relative;
    width: 971px;
    height: 1200px;
    overflow: hidden;
    font-family: 'Oswald', 'Arial Narrow', sans-serif;
    color: var(--white);
  }
  .spotlight-card p, .spotlight-card h1, .spotlight-card blockquote { white-space: nowrap; }
  .card-background { position: absolute; inset: 0; }
  .brand-name {
    position: absolute;
    right: 93px;
    top: 83px;
    font-weight: 600;
    font-size: 66px;
    line-height: 66px;
    letter-spacing: 1px;
    color: var(--navy);
  }
  .member-name {
    position: absolute;
    left: 468px;
    top: 230px;
    font-weight: 700;
    font-size: 78px;
    line-height: 88px;
    color: var(--ink);
    letter-spacing: -1px;
  }
  .member-role {
    position: absolute;
    left: 477px;
    top: 417px;
    font-weight: 400;
    font-size: 32px;
    line-height: 40px;
    letter-spacing: -0.5px;
    color: var(--ink);
  }
  .stat {
    position: absolute;
    text-align: center;
    width: 460px;
  }
  .stat-left { left: 62px; width: 460px; left: 61px; }
  .stat-left { left: 60px; width: 466px; left: 59px; }
  .stat-left { left: 58px; width: 470px; left: 57px; }
  .stat-left { left: 57px; width: 470px; transform: translateX(-45px); }
  .stat-right { left: 498px; }
  .stat-label {
    font-weight: 300;
    font-size: 26px;
    line-height: 32px;
    letter-spacing: -0.5px;
  }
  .stat-value {
    font-weight: 600;
    font-size: 72px;
    line-height: 78px;
    letter-spacing: -1px;
  }
  .stat-value.is-medium { font-size: 46px; line-height: 52px; margin-top: 6px; }
  .stat-value.is-long { font-size: 36px; line-height: 44px; margin-top: 14px; }
  .stat-note {
    font-weight: 300;
    font-style: italic;
    font-size: 19px;
    line-height: 22px;
    color: var(--magenta);
  }
  .stat-tenure .stat-note { margin-top: 8px; font-size: 17px; }
  .stat-hobby .stat-note { margin-top: 10px; }
  .stat-years { top: 676px; }
  .stat-tenure { top: 862px; }
  .stat-hobby { top: 676px; }
  .stat-football { top: 862px; }
  .football-icon { display: inline-block; vertical-align: -5px; margin-left: 4px; }
  .column-divider {
    position: absolute;
    left: 484px;
    top: 648px;
    width: 2px;
    height: 347px;
    background: var(--magenta);
  }
  .quote-label {
    position: absolute;
    left: 0;
    width: 971px;
    top: 1014px;
    text-align: center;
    font-weight: 300;
    font-size: 27px;
    line-height: 40px;
    letter-spacing: -0.5px;
  }
  .quote-box {
    position: absolute;
    left: 129px;
    top: 1065px;
    width: 713px;
    height: 66px;
    background: var(--magenta);
    display: flex;
    align-items: center;
    justify-content: center;
    font-weight: 600;
    font-size: 27px;
    line-height: 1;
    letter-spacing: -0.6px;
  }
  .quote-pointer { position: absolute; left: 793px; top: 1130px; }
  .quote-author {
    position: absolute;
    right: 118px;
    top: 1149px;
    font-weight: 300;
    font-style: italic;
    font-size: 22px;
    line-height: 34px;
    letter-spacing: -0.3px;
  }
</style>
</head>
<body>
<main class="spotlight-card">
  <svg class="card-background" width="971" height="1200" viewBox="0 0 971 1200">
    <defs>
      <linearGradient id="header-wash" x1="0" y1="0" x2="0.35" y2="1">
        <stop offset="0" stop-color="#f2a9dc"/>
        <stop offset="0.45" stop-color="#fbe3f3"/>
        <stop offset="0.8" stop-color="#ffffff"/>
      </linearGradient>
      <linearGradient id="portrait-tone" x1="0" y1="0" x2="0" y2="1">
        <stop offset="0" stop-color="#e9d3cf"/>
        <stop offset="0.45" stop-color="#c9a595"/>
        <stop offset="0.62" stop-color="#2f4f86"/>
        <stop offset="1" stop-color="#1e3868"/>
      </linearGradient>
    </defs>
    <rect class="header-wash" x="0" y="0" width="971" height="660" fill="url(#header-wash)"/>
    <rect class="portrait" x="0" y="90" width="510" height="560" fill="url(#portrait-tone)" role="img" aria-label="Portrait photo of Cole Banner in a navy suit and tie"/>
    <polygon class="accent-band" points="0,626 971,513 971,526 0,651" fill="var(--magenta)"/>
    <polygon class="stats-panel" points="0,651 971,526 971,1200 0,1200" fill="var(--navy)"/>
  </svg>

  <div class="brand-name">ORLO SPAN KT</div>

  <h1 class="member-name">COLE<br>BANNER</h1>
  <p class="member-role">AREA SALES MANAGER - AUSTIN, TX</p>

  <section class="stat stat-left stat-years">
    <p class="stat-label">YEARS IN PAIN MANAGEMENT</p>
    <p class="stat-value">8 YEARS</p>
  </section>

  <section class="stat stat-left stat-tenure">
    <p class="stat-label">TIME AT ORLO SPAN KT</p>
    <p class="stat-value">1 YEAR</p>
    <p class="stat-note">(BY FEBRUARY)</p>
  </section>

  <div class="column-divider"></div>

  <section class="stat stat-right stat-hobby">
    <p class="stat-label">HOBBY/PASSION</p>
    <p class="stat-value is-medium">MAKING MUSIC</p>
    <p class="stat-note">(ON TUNEVO AS COLE BANNER!)</p>
  </section>

  <section class="stat stat-right stat-football">
    <p class="stat-label">FOOTBALL TEAM
      <svg class="football-icon" width="32" height="26" viewBox="0 0 32 26" aria-hidden="true">
        <ellipse cx="16" cy="13" rx="14" ry="8" transform="rotate(-30 16 13)" fill="none" stroke="var(--white)" stroke-width="2"/>
        <line x1="10" y1="17" x2="22" y2="9" stroke="var(--magenta)" stroke-width="2"/>
        <line x1="13" y1="12" x2="15" y2="15" stroke="var(--white)" stroke-width="1.5"/>
        <line x1="16" y1="10" x2="18" y2="13" stroke="var(--white)" stroke-width="1.5"/>
        <line x1="19" y1="8" x2="21" y2="11" stroke="var(--white)" stroke-width="1.5"/>
      </svg>
    </p>
    <p class="stat-value is-long">RIDGEFORD STATE (HAWKLETS)</p>
  </section>

  <p class="quote-label">FAVORITE QUOTE</p>
  <blockquote class="quote-box">“NOTHING IN THE WORLD CAN TAKE THE PLACE OF PERSISTENCE.”</blockquote>
  <svg class="quote-pointer" width="26" height="22" viewBox="0 0 26 22" aria-hidden="true">
    <polygon points="0,0 26,0 13,22" fill="var(--magenta)"/>
  </svg>
  <p class="quote-author">HAROLD PEMBERTON</p>
</main>
</body>
</html>
```